Theatrical Producer/Consultant needs Artistic Brochure Shell and Inserts

Heron Stageworks (www.heronstageworks-example.com) is a small company that offers theatrical producing and consulting services. We would like to create a brochure that contains information about our various productions and services. Because our roster is fluid, we are proposing to create a brochure shell or folder with pockets, and then a template for individual tear sheets that would be inserted into the inside pockets of the brochure shell/folder. The shell is intended for reuse each season, and new tear sheets will be developed separately on a project by project basis.
This task is to create the shell and a corresponding tear sheet template.
The brochure will be delivered by hand as well as by mail, so should fit into a standard size mailing envelope (i.e., within NPMS flat dimensions of 6 1/8" x 11 1/2")
The final design should reflect the high level of artistry of our theatrical projects. Attached are our logo as well as photos of current theatrical offerings which are available for use on the brochure shell but not required. There is also a file that describes our services in more detail, fyi. This will ultimately go onto one of the tear sheets in the brochure.
For the tear sheet template, we have also included a sample brochure from a peer colleague, just to give you an idea of the kind of information each sheet would contain. Each project page will contain title of the project, information about the artists involved, one or more photos, a project description, schedule, fee and other technical information.
The final files for both the shell and tear sheet templates should be printer-ready and also in a file format that we can edit ourselves in future.
Updates
Project Deadline Extended Reason: There was a discrepancy between posted project deadline (December 7) and when project was automatically closed (December 6). Since several designers who have not yet submitted indicated they were planning to submit designs, we wanted to make sure that they were able to do so. Added Monday, December 7, 2015
Industry/Entity Type
Performing Art
Font styles to use
Look and feel
Each slider illustrates characteristics of the customer's brand and the style your logo design should communicate.

```html
<!DOCTYPE html>
<html lang="en">
<head>
<meta charset="utf-8">
<title>Heron Stageworks – New Productions Tear Sheet</title>
<link rel="stylesheet" href="https://fonts.googleapis.com/css2?family=Arvo:wght@700&family=Ubuntu:wght@300;400;700&display=swap">
<style>
  :root {
    --teal: #1f9fb5;
    --ink: #1b1b1b;
    --text: #3a3a3a;
    --paper: #ffffff;
    --backdrop: #ececee;
    --photo-dark: #5a5a5a;
    --photo-light: #c9c9c9;
  }
  * { margin: 0; padding: 0; box-sizing: border-box; }
  html, body { width: 1200px; height: 1000px; overflow: hidden; }
  body {
    background: var(--backdrop);
    font-family: "Ubuntu", sans-serif;
    font-weight: 300;
    color: var(--text);
  }
  .tear-sheet {
    position: absolute;
    left: 380px; top: 30px;
    width: 440px; height: 940px;
    background: var(--paper);
    box-shadow: 0 4px 18px rgba(0,0,0,0.12);
  }
  .sheet-header {
    position: absolute; top: 40px; left: 92px;
    display: flex; align-items: center; gap: 14px;
  }
  .rule { display: block; height: 4px; background: var(--teal); }
  .sheet-header .rule { width: 50px; }
  .sheet-header h1 {
    font-family: "Arvo", serif; font-weight: 700;
    font-size: 21px; letter-spacing: 0.5px; color: var(--ink);
  }
  .production-photo {
    position: absolute; left: 0; top: 118px;
    width: 172px; height: 160px;
    background: radial-gradient(circle at 55% 45%, var(--photo-light), var(--photo-dark));
  }
  .photo-rule { position: absolute; left: 122px; top: 290px; width: 50px; }
  .production-main {
    position: absolute; left: 186px; top: 112px; width: 240px;
  }
  .production-title {
    font-family: "Arvo", serif; font-weight: 700;
    font-size: 19px; color: var(--teal); letter-spacing: 0.5px;
  }
  .production-main .rule { width: 52px; height: 3px; margin: 8px 0 12px; }
  .synopsis { font-size: 13px; line-height: 19.5px; }
  .main-notes {
    margin-top: 12px;
    font-size: 9.5px; line-height: 12px;
  }
  .credits {
    position: absolute; left: 14px; top: 304px; width: 158px;
    text-align: right; font-size: 11px; line-height: 14px;
  }
  .credits .source { margin-bottom: 8px; font-size: 11.5px; }
  .credits dt { color: var(--teal); margin-top: 6px; }
  .credits .meta { color: var(--teal); margin-top: 8px; }
  .credits .meta span { color: var(--text); }
  .side-notes {
    position: absolute; left: 14px; top: 632px; width: 158px;
    text-align: right; font-size: 10px; line-height: 13px;
  }
  .side-notes p + p { margin-top: 2px; }
  .side-notes strong { font-weight: 700; color: var(--ink); }
  .dates {
    position: absolute; left: 186px; top: 700px; width: 240px;
  }
  .dates h2 {
    font-weight: 300; font-size: 16px; color: var(--teal); letter-spacing: 0.5px;
  }
  .dates .rule { width: 56px; height: 3px; margin: 8px 0 12px; }
  .dates ul { list-style: none; font-size: 10px; line-height: 12px; }
  .dates li { margin-bottom: 2px; }
  .dates b { font-weight: 700; color: var(--ink); display: block; }
  .brand {
    position: absolute; left: 22px; top: 812px; width: 150px;
    display: flex; align-items: center; gap: 6px;
  }
  .brand-dot { flex: none; width: 16px; height: 16px; border-radius: 50%; background: var(--teal); }
  .brand-name { font-size: 14px; font-weight: 400; color: var(--ink); white-space: nowrap; }
</style>
</head>
<body>
  <article class="tear-sheet">
    <header class="sheet-header">
      <span class="rule"></span>
      <h1>NEW PRODUCTIONS</h1>
    </header>

    <div class="production-photo" role="img" aria-label="Black and white portrait photograph of the production's director"></div>
    <span class="rule photo-rule"></span>

    <section class="production-main">
      <h2 class="production-title">RIVERFIELD</h2>
      <span class="rule"></span>
      <p class="synopsis">Lorem ipsum dolor sit amet, consectetur adipisicing elit, sed do eiusmod tempor incididunt ut labore et dolore magna aliqua. Ut enim ad minim veniam, quis nostrud exercitation. Lorem ipsum dolor sit amet, consectetur adipisicing elit, sed do eiusmod tempor incididunt ut labore et dolore magna aliqua. Ut enim ad minim veniam, quis nostrud exercitation. Lorem ipsum dolor sit amet, consectetur adipisicing elit, sed do eiusmod tempor incididunt ut labore et dolore magna aliqua. Ut enim ad minim veniam, quis nostrud exercitation. Lorem ipsum dolor sit amet, consectetur adipisicing elit, sed do eiusmod tempor incididunt ut labore et dolore magna aliqua. Ut enim ad minim veniam, quis nostrud exercitation.</p>
      <div class="main-notes">
        <p>Lorem ipsum dolor sit amet, consectetur adipisicing elit, sed do eiusmod tempor incididunt ut labore et dolore magna aliqua.</p>
        <p>Lorem ipsum dolor sit amet, consectetur adipisicing elit, sed do eiusmod tempor incididunt ut labore et dolore magna aliqua.</p>
      </div>
    </section>

    <dl class="credits">
      <div class="source">Based on Mahabharta</div>
      <dt>Text by</dt>
      <dd>Paul Arden, Jean-Luc Morel and Marie Claire Estève</dd>
      <dt>Directed by</dt>
      <dd>Paul Arden and Marie Claire Estève</dd>
      <dt>Music</dt>
      <dd>Kenji Moriyama</dd>
      <dt>Lighting</dt>
      <dd>Philippe Varenne</dd>
      <dt>With</dt>
      <dd>Celine Kamanzi, Jordan McKay, Eli Ndayisaba and Sean O'Rourke</dd>
      <div class="meta">Show Performed in English</div>
      <div class="meta" style="margin-top:2px">Duration: <span>1h 30min (tbc)</span></div>
    </dl>

    <div class="side-notes">
      <p>Lorem ipsum dolor sit amet, consectetur adipisicing elit, sed do eiusmod tempor incididunt ut labore et dolore magna aliqua.</p>
      <p><strong>Lorem ipsum dolor sit amet, consectetur adipisicing elit, sed do eiusmod tempor incididunt ut labore et dolore magna aliqua.</strong></p>
    </div>

    <section class="dates">
      <h2>PERFORMANCE DATES</h2>
      <span class="rule"></span>
      <ul>
        <li><b>Sept. 15 to Oct. 17, 2015</b>Théâtre du Quai Vert</li>
        <li><b>Nov. 17 to 21, 2015</b>Harbourline Repertory Theatre/Singapore</li>
        <li><b>Nov. 25 to 29, 2015</b>Kasumi Theatre/Tokyo/Japan</li>
        <li><b>Dec. 10 to 11, 2015</b>Maison des Arts d'Amiens</li>
        <li><b>Feb. 3 to 27, 2016</b>Old Wharf Theatre/London/Great Britain</li>
        <li><b>March. 5 to 12, 2016</b>Mumbai/India</li>
      </ul>
    </section>

    <footer class="brand">
      <span class="brand-dot"></span>
      <span class="brand-name">Heron Stageworks</span>
    </footer>
  </article>
</body>
</html>
```